"Made in Chicago" Baby Shower Invitation

I need a design for a baby shower invitation with the headline and theme of "Made in Chicago". The design should incorporate the colors/design of the Chicago flag. I have attached an image of the flag for your reference. The design should be sized 5-1/2 wide x 8-1/2 long. I want to be able to print two to a page on a standard 8-1/2 X 11" piece of (nice quality) paper on a standard home printer.
Copy:
Made in Chicago Baby Shower
For: Marla & Gordon
Date: Saturday, April 5, 2014
Time: 7:00 p.m.
Place: 27 West Halbrook Ave, 4B
RSVP by April 1 to Nadia Verholm/312-555-0193

Hello Designers - I corrected the size requirements of the invitation (bad math before) and added a few more notes of preference. Looking for a design that is more clean and graphic and less traditional, soft baby shower look. Thank you!

Friends & family of the 20-sometthing, urban professional couple who are having a baby.

Baby

Must have
• Chicago flag colors and/or image, the words "made in Chicago", and the (revised) size indicated.
Should not have
• Anything inappropriate or offensive to grandmother of said couple.

```html
<!DOCTYPE html>
<html lang="en">
<head>
<meta charset="utf-8">
<title>Made in Chicago Baby Shower Invitation</title>
<link rel="stylesheet" href="https://fonts.googleapis.com/css2?family=Chewy&family=Fira+Sans+Condensed:ital,wght@1,500&family=Noto+Serif&display=swap">
<style>
  :root {
    --accent-red: #f50f0f;
    --band-blue: #b5dcf0;
    --skyline-blue: #dcecf8;
    --paper: #ffffff;
    --backdrop: #000000;
  }
  * { box-sizing: border-box; margin: 0; padding: 0; }
  html, body {
    width: 1200px; height: 1000px; overflow: hidden;
    background: var(--backdrop);
  }
  .invitation {
    position: absolute; left: 410px; top: 120px;
    width: 380px; height: 760px;
    background: var(--accent-red);
  }
  .border-decoration {
    position: absolute; inset: 0;
    background: var(--accent-red);
  }
  .panel {
    position: absolute; left: 45px; top: 45px;
    width: 290px; height: 670px;
    background: var(--paper);
    overflow: hidden;
    text-align: center;
    color: var(--accent-red);
  }
  .skyline {
    position: absolute; left: 0; right: 0; bottom: 0; height: 300px;
    background: linear-gradient(to bottom, rgba(220,236,248,0) 0%, var(--skyline-blue) 45%, var(--skyline-blue) 100%);
  }
  .headline {
    position: absolute; top: 12px; left: 0; right: 0;
    font-family: "Noto Serif", Georgia, serif;
    font-weight: 400;
    font-size: 27px; letter-spacing: 0.5px;
  }
  .flag-band {
    position: absolute; left: 0; right: 0; top: 62px; height: 114px;
    background: linear-gradient(to bottom, var(--band-blue) 0%, #e4f2fa 50%, var(--band-blue) 100%);
  }
  .event-title {
    position: absolute; left: 0; right: 0;
    font-family: "Chewy", "Comic Sans MS", cursive;
    font-weight: 400;
    line-height: 1;
  }
  .event-title.baby {
    top: 212px; font-size: 68px;
    color: var(--paper);
    -webkit-text-stroke: 3px var(--accent-red);
    text-shadow: 4px 4px 0 var(--accent-red);
  }
  .event-title.shower { top: 290px; font-size: 66px; }
  .details {
    position: absolute; top: 392px; left: 0; right: 0;
    list-style: none;
    font-family: "Fira Sans Condensed", "Arial Narrow", sans-serif;
    font-style: italic; font-weight: 500;
  }
  .details li { height: 44px; font-size: 18px; line-height: 24px; }
  .details .rsvp { font-size: 15px; }
  .details .phone { font-size: 17px; }
</style>
</head>
<body>
  <article class="invitation">
    <div class="border-decoration" role="img" aria-label="Red frame decorated with white six-pointed stars"></div>

    <section class="panel">
      <div class="skyline" role="img" aria-label="Faint light blue city skyline silhouette"></div>

      <h2 class="headline">Made in Chicago</h2>
      <div class="flag-band" role="img" aria-label="City flag motif with light blue stripes and red stars"></div>

      <h1 class="event-title baby">Baby</h1>
      <h1 class="event-title shower">Shower</h1>

      <ul class="details">
        <li>For Marla &amp; Gordon</li>
        <li>on Saturday, April 5, 2014</li>
        <li>7.00 p.m. onwards</li>
        <li>at 27 West Halbrook Ave, 4B</li>
        <li class="rsvp">RSVP by April 1 to Nadia Verholm</li>
        <li class="phone">312-555-0193</li>
      </ul>
    </section>
  </article>
</body>
</html>
```